Business Card Design

we need a business card as well as a logo that can be used for signs etc.
this is a very formal, classy , elegant function centre, as well as café. I am after a design that stands out and grabs people attentions. my colours theme is really warm ,colours like chocolate browns, and latte type colours with really deep red tones
not bright red, just warm tones. this is a place that very wealthy and maybe even celebs will come so I need it to be appealing.
Industry/Entity Type
Business
Contact Information for Business Card
Grey Finch
café and function centre @ haldons estate.
wedding and function specialists,
Corbett highway, lucknow,ph 0427385190

```html
<!DOCTYPE html>
<html lang="en">
<head>
<meta charset="utf-8">
<title>Grey Finch cafe &amp; function centre – business card</title>
<link rel="stylesheet" href="https://fonts.googleapis.com/css2?family=Fondamento&family=Cormorant+Garamond:wght@400;500&display=swap">
<style>
  :root {
    --page-bg: #efe7dc;
    --card-red: #a81d38;
    --card-red-deep: #8c1430;
    --band-red: #7c1029;
    --band-line: #c9953f;
    --title-cream: #f6e4c4;
    --tagline-rose: #d9a2b4;
    --contact-gold: #e8b95c;
    --contact-rose: #cf8a6c;
    --badge-fill: #eab8a6;
    --motif-warm: #d9573d;
    --motif-dark: #6d0f24;
  }
  html, body {
    margin: 0;
    width: 1200px;
    height: 900px;
    overflow: hidden;
    background: var(--page-bg);
  }
  .canvas {
    position: relative;
    width: 1200px;
    height: 900px;
  }
  .business-card {
    position: absolute;
    left: 100px;
    top: 150px;
    width: 1000px;
    height: 600px;
    border-radius: 24px;
    overflow: hidden;
    box-shadow: 0 18px 40px rgba(60, 20, 20, 0.25);
  }
  .business-card svg { display: block; }
  .title-text {
    font-family: "Fondamento", cursive;
    font-size: 60px;
    fill: var(--title-cream);
  }
  .tagline {
    font-family: "Cormorant Garamond", serif;
    font-size: 27px;
    letter-spacing: 2px;
    fill: var(--tagline-rose);
  }
  .contact-name {
    font-family: "Fondamento", cursive;
    font-size: 35px;
    fill: var(--contact-gold);
  }
  .contact-details {
    font-family: "Cormorant Garamond", serif;
    font-size: 28px;
    fill: var(--contact-rose);
  }
  .contact-details .small { font-size: 23px; }
</style>
</head>
<body>
<main class="canvas">
  <section class="business-card" aria-label="Grey Finch cafe and function centre business card">
    <svg width="1000" height="600" viewBox="0 0 1000 600">
      <defs>
        <linearGradient id="card-fill" x1="0" y1="0" x2="1" y2="1">
          <stop offset="0" stop-color="var(--card-red)"/>
          <stop offset="1" stop-color="var(--card-red-deep)"/>
        </linearGradient>
        <radialGradient id="flower-glow" cx="0.5" cy="0.5" r="0.5">
          <stop offset="0" stop-color="var(--motif-warm)" stop-opacity="0.55"/>
          <stop offset="1" stop-color="var(--motif-warm)" stop-opacity="0"/>
        </radialGradient>
        <radialGradient id="swirl-shade" cx="0.5" cy="0.5" r="0.5">
          <stop offset="0" stop-color="var(--motif-dark)" stop-opacity="0.35"/>
          <stop offset="1" stop-color="var(--motif-dark)" stop-opacity="0"/>
        </radialGradient>
        <path id="title-arc" d="M50,262 Q480,70 960,212"/>
      </defs>

      <rect class="card-base" width="1000" height="600" fill="url(#card-fill)"/>

      <ellipse class="swirl-decoration" role="img" aria-label="Faint swirling vine ornament along the left edge" cx="180" cy="260" rx="200" ry="260" fill="url(#swirl-shade)"/>
      <ellipse class="swirl-decoration" role="img" aria-label="Faint branching vine ornament in the top right corner" cx="900" cy="90" rx="180" ry="140" fill="url(#swirl-shade)"/>
      <ellipse class="flower-decoration" role="img" aria-label="Soft glowing flower ornament in the centre" cx="440" cy="380" rx="150" ry="140" fill="url(#flower-glow)"/>

      <text class="title-text">
        <textPath href="#title-arc" startOffset="1%">Grey Finch cafe</textPath>
      </text>
      <circle class="title-badge" cx="500" cy="156" r="24" fill="var(--badge-fill)"/>
      <text class="title-text">
        <textPath href="#title-arc" startOffset="55%">function centre</textPath>
      </text>

      <text class="tagline" x="262" y="262" transform="rotate(-3 262 262)">WEDDING &#160;&amp;&#160; FUNCTION</text>

      <path class="contact-band" d="M0,498 Q480,392 1000,398 L1000,600 L0,600 Z" fill="var(--band-red)"/>
      <path class="band-line" d="M0,498 Q480,392 1000,398" fill="none" stroke="var(--band-line)" stroke-width="3"/>

      <g transform="rotate(-4 60 530)">
        <text class="contact-name" x="60" y="522">Grey Finch cafe and function centre@haldons estate</text>
        <text class="contact-details" x="60" y="570">Wedding and function specalists, <tspan class="small">Corbett highway, Ashvale,</tspan></text>
        <g class="phone-icon" transform="translate(780 562)">
          <circle r="10" fill="none" stroke="var(--contact-rose)" stroke-width="2"/>
          <path d="M-4,-5 q-2,6 4,10 l2,-2 -2,-2 -1,1 q-2,-2 -2,-4 l1,-1 -2,-2 z" fill="var(--contact-rose)"/>
        </g>
        <text class="contact-details" x="798" y="570"><tspan class="small">0427385190</tspan></text>
      </g>
    </svg>
  </section>
</main>
</body>
</html>
```